program promotional Information booklets used for marketing and information

We need someone to take our two word documents and work some graphic design magic to make it look more professional and inviting. These documents are used for potential new customers. Our target audience is youth and young adults with disabilities and their families. Our website will help to provide our current style www.brightpathways.com.au and our logo will set the colour palette. We want the booklets to convey a culture of fun, innovation, energy & creativity. We do not want to look like a corporate or formal organisation. We want to look more organic and grassroots. The booklets will be distributed as electronic documents and printed in-house. Ideally we would like to still be able to edit the final document in case our prices or services change in the future.

Target Market(s)

Youth and Young adults with special needs

Industry/Entity Type

Community Service

Font styles to use
Sans Serif

Requirements
Must have
• The photos provided relate to the Wayfinder booklet. This program is for those with more profound disabilities. The Uplift program is for those with less support needs, generally not in wheelchairs, but who may have some mobility challenges and mild intellectual disabilities. As you will see our business name is Bright Pathways and this is what we attempt to do for all the young people we work with. We do not focus on their disability but rather on their unique abilities and what they can achieve. In both programs we look to achieve social inclusion in the general community as much as possible.
Nice to have
• Wants to feel high energy, fun, innovative and creative. Could use some stock images in the Uplift booklet if you wanted to. Some of the activities this program will do include: organic gardening, cooking, music, dance and drama, art, life skills, mastering public transport, exercise, etc.
Should not have
• should not focus on disability stereotypes. Should not be too childish.

```html
<!DOCTYPE html>
<html lang="en">
<head>
<meta charset="utf-8">
<title>Wayfinder Information Booklet – Bright Pathways</title>
<link rel="stylesheet" href="https://fonts.googleapis.com/css2?family=Saira+Semi+Condensed:wght@500;700&family=Montserrat:wght@500&display=swap">
<style>
  :root {
    --purple: #9a69aa;
    --charcoal: #646464;
    --slate: #7a7a7a;
    --band: #d7d7d7;
    --teal: #5bb6b1;
    --orange: #ee8b36;
    --coral: #ef5b5b;
    --olive: #c9ad3c;
    --paper: #ffffff;
  }
  html, body {
    margin: 0;
    padding: 0;
    overflow: hidden;
    background: var(--paper);
  }
  .booklet-cover {
    position: relative;
    width: 848px;
    height: 1200px;
    overflow: hidden;
    background: var(--paper);
    font-family: "Saira Semi Condensed", "Arial Narrow", sans-serif;
  }
  .brand-name {
    position: absolute;
    left: 79px;
    top: 282px;
    margin: 0;
    font-family: "Montserrat", Arial, sans-serif;
    font-weight: 500;
    font-size: 40px;
    color: var(--purple);
    letter-spacing: 0.2px;
  }
  .cover-title {
    position: absolute;
    left: 78px;
    top: 486px;
    margin: 0;
    font-weight: 700;
    line-height: 0.98;
  }
  .cover-title .program-name {
    display: block;
    font-size: 80px;
    font-style: italic;
    color: var(--purple);
    text-transform: uppercase;
    letter-spacing: 0.5px;
  }
  .cover-title .doc-type {
    display: block;
    font-size: 88px;
    color: var(--charcoal);
  }
  .contact-band {
    position: absolute;
    left: 0;
    top: 970px;
    width: 848px;
    height: 184px;
    background: var(--band);
  }
  .contact-list {
    position: absolute;
    left: 79px;
    top: 1008px;
    margin: 0;
    padding: 0;
    list-style: none;
    font-size: 17.5px;
    line-height: 25px;
    color: var(--slate);
    font-weight: 500;
  }
  .contact-list .label {
    font-weight: 700;
    color: #4a4a4a;
  }
  .contact-list .indent {
    padding-left: 8px;
  }
  .tree-artwork {
    position: absolute;
    left: 470px;
    top: 36px;
    width: 378px;
    height: 1164px;
    background:
      radial-gradient(ellipse at 70% 12%, rgba(91,182,177,0.35), transparent 55%),
      radial-gradient(ellipse at 40% 40%, rgba(238,139,54,0.30), transparent 55%),
      radial-gradient(ellipse at 75% 62%, rgba(154,105,170,0.30), transparent 55%),
      radial-gradient(ellipse at 35% 82%, rgba(239,91,91,0.30), transparent 50%),
      linear-gradient(180deg, rgba(201,173,60,0.10), rgba(100,100,100,0.35));
    border-top-left-radius: 190px;
  }
</style>
</head>
<body>
  <main class="booklet-cover">
    <p class="brand-name">Bright Pathways</p>

    <h1 class="cover-title">
      <span class="program-name">Wayfinder</span>
      <span class="doc-type">Information</span>
      <span class="doc-type">Booklet</span>
    </h1>

    <div class="contact-band"></div>
    <ul class="contact-list">
      <li><span class="label">Hub Locations:</span> 41 Harbour St, Kellow</li>
      <li class="indent">5/210 Wattle Rd, Ridgeview</li>
      <li><span class="label">Email:</span> info@brightpathways.com.au</li>
      <li><span class="label">Postal Address:</span> PO Box 22, Greenvale DC, 4099</li>
      <li><span class="label">Phone:</span> 1300 555 019</li>
    </ul>

    <div class="tree-artwork" role="img" aria-label="Large decorative tree with colourful teal, orange, purple, coral and olive leaves rising along the right edge"></div>
  </main>
</body>
</html>
```